Event flyer for Sunday night Youth Group

Need a 4 x 6 or 5 x 7 flyer for a new youth group starting on April 14. The youth group is for students in middle school and high school so it needs to look fun and cool, but not childish. I prefer it not to include pictures of people unless it's so obscure you can't really see their faces. I've uploaded some pictures of flyers I like. I've also attached a couple versions of our logo to use on the flyer.
Information the flyer needs to include:
Youth Group
Sundays, 6-8pm (beginning April 14)
Location: Merriwick's - 4219 Hollowfern Ln S, Keizer, 97418
There will be dinner, games, friends, and a message.
Target Market(s)
Youth ages 13-18
Industry/Entity Type
Church
Colors
Designer to choose colors to be used in the design.
Look and feel

```html
<!DOCTYPE html>
<html lang="en">
<head>
<meta charset="UTF-8">
<title>Youth Group Flyer</title>
<link href="https://fonts.googleapis.com/css2?family=Anton&family=Kaushan+Script&family=Open+Sans:wght@600;700;800&display=swap" rel="stylesheet">
<style>
  :root {
    --backdrop: #4a4a4a;
    --flame: #d9452a;
    --ember: #e8703a;
    --glow: #fbe7a0;
    --ink: #0c0c0c;
    --mint: #7ee0c3;
    --accent-red: #d63a1e;
    --gold: #e6b12c;
    --paper-white: #ffffff;
  }
  * { margin: 0; padding: 0; box-sizing: border-box; }
  html, body {
    width: 1200px; height: 2167px; overflow: hidden;
    background: var(--backdrop);
  }
  .flyer {
    position: absolute;
    left: 40px; top: 302px;
    width: 1120px; height: 1563px;
    overflow: hidden;
    background:
      radial-gradient(ellipse 520px 620px at 50% 800px, var(--glow) 0%, #f6c66a 30%, rgba(236,130,70,0) 75%),
      linear-gradient(180deg, var(--flame) 0%, var(--ember) 40%, var(--flame) 80%);
    box-shadow: 0 10px 30px rgba(0,0,0,.45);
    font-family: "Open Sans", sans-serif;
  }
  .brand {
    position: absolute; top: 200px; left: 0; right: 0; z-index: 2;
    display: flex; align-items: center; justify-content: center; gap: 14px;
  }
  .brand-dot {
    width: 30px; height: 30px; border-radius: 50%; background: var(--ink);
  }
  .brand-name {
    font-weight: 700; font-size: 36px; letter-spacing: 3px;
    color: var(--ink); text-transform: uppercase;
  }
  .title-script {
    position: absolute; top: 140px; left: 0; right: 0; z-index: 1;
    text-align: center;
    font-family: "Kaushan Script", cursive;
    font-size: 360px; line-height: 1;
    transform: scaleY(1.35); transform-origin: 50% 0;
  }
  .title-script span {
    display: inline-block;
    padding: 0 30px;
    background: linear-gradient(180deg, var(--mint) 10%, #3f8f78 45%, var(--ink) 78%);
    -webkit-background-clip: text; background-clip: text;
    color: transparent;
    filter: drop-shadow(3px 4px 0 var(--accent-red));
  }
  .title-block {
    position: absolute; top: 470px; left: 0; right: 0; z-index: 3;
    text-align: center;
    font-family: "Anton", sans-serif;
    font-size: 250px; line-height: 1;
    color: var(--paper-white);
    -webkit-text-stroke: 4px #3a2a14;
  }
  .schedule {
    position: absolute; top: 742px; left: 0; right: 0; text-align: center;
    font-family: "Anton", sans-serif; font-size: 120px; line-height: 1;
    color: var(--ink);
  }
  .start-date {
    position: absolute; top: 868px; left: 0; right: 0; text-align: center;
    font-weight: 800; font-size: 70px; line-height: 1;
    color: var(--accent-red);
  }
  .crowd {
    position: absolute; left: 0; right: 0; top: 960px; bottom: 0;
    background: linear-gradient(180deg, rgba(12,12,12,0) 0%, rgba(12,12,12,.55) 30%, var(--ink) 55%, var(--ink) 100%);
  }
  .info-box {
    position: absolute; top: 1319px; height: 232px;
    border: 2px dashed #8a6a1c; border-radius: 14px;
  }
  .info-box--left { left: 52px; width: 452px; padding: 22px 18px; }
  .info-box--right { left: 604px; width: 466px; padding: 44px 14px; }
  .divider {
    position: absolute; left: 554px; top: 1330px; width: 2px; height: 210px;
    background: var(--paper-white);
  }
  .info-label {
    color: var(--paper-white); font-weight: 600; font-size: 38px; line-height: 1.2;
  }
  .info-list {
    color: var(--mint); font-weight: 800; font-size: 47px; line-height: 0.98;
    text-transform: uppercase; margin-top: 8px;
  }
  .contact-row { display: flex; align-items: center; gap: 12px; }
  .contact-row + .contact-row { margin-top: 26px; }
  .contact-row svg { flex: none; }
  .address {
    color: var(--paper-white); font-weight: 600; font-size: 23px; line-height: 1.3;
    white-space: nowrap;
  }
  .website { color: var(--mint); font-weight: 800; font-size: 30px; white-space: nowrap; }
</style>
</head>
<body>
  <main class="flyer">
    <div class="brand">
      <span class="brand-dot"></span>
      <span class="brand-name">Waypoint Fellowship</span>
    </div>

    <div class="title-script"><span>Youth</span></div>
    <div class="title-block">Group</div>

    <div class="schedule">SUNDAYS 6-8PM</div>
    <div class="start-date">Beginning April 14</div>

    <div class="crowd" role="img" aria-label="Silhouettes of a cheering crowd with raised arms against the glow"></div>

    <section class="info-box info-box--left">
      <p class="info-label">THERE WILL BE :</p>
      <p class="info-list">Dinner, games,<br>friends, and<br>a message.</p>
    </section>

    <div class="divider"></div>

    <section class="info-box info-box--right">
      <div class="contact-row">
        <svg width="44" height="50" viewBox="0 0 52 56" aria-hidden="true">
          <path d="M26 4a13 13 0 0 1 13 13c0 10-13 25-13 25S13 27 13 17A13 13 0 0 1 26 4z" fill="var(--gold)"/>
          <circle cx="26" cy="17" r="5" fill="#0c0c0c"/>
          <ellipse cx="26" cy="47" rx="20" ry="6" fill="none" stroke="var(--gold)" stroke-width="3"/>
        </svg>
        <p class="address">Merriwick's - 4219 Hollowfern<br>Ln S, Keizer, 97418</p>
      </div>
      <div class="contact-row">
        <svg width="44" height="36" viewBox="0 0 52 40" aria-hidden="true">
          <circle cx="26" cy="20" r="17" fill="var(--gold)"/>
          <g fill="none" stroke="#0c0c0c" stroke-width="2">
            <circle cx="26" cy="20" r="10"/>
            <ellipse cx="26" cy="20" rx="4.5" ry="10"/>
            <line x1="16" y1="20" x2="36" y2="20"/>
          </g>
        </svg>
        <p class="website">www.waypoint.org</p>
      </div>
    </section>
  </main>
</body>
</html>
```